Maritime Law Firm Business Card Design Project

We are a new maritime law firm starting in Queensland, Australia. The principal is a master mariner as well as a lawyer and is looking for a logo design that evokes a practical and user-friendly approach to the law, as well as maritime law expertise.

We would like to use the compass rose as the foundation for the design, as it symbolises clarity of direction and purpose, as well as traditional maritime heritage.

The 16th Century Lluc Ferrandis Compass Rose (attached) is beautiful, but is too complex for a logo. A simplified version is desired.

Colour Paletter s flexible, although a B&W version is also needed. Colour suggestions are navy blue (for the sea), red and green (navigation lights) and maroon (for Queensland).

Target Market(s)

Maritime Industry/legal services

Industry/Entity Type

Law Firm

Font styles to use
Sans Serif

Requirements
Must have
• Contact Details
Name of 'Pellworth Legal'

```html
<!DOCTYPE html>
<html lang="en">
<head>
<meta charset="utf-8">
<title>Pellworth Legal – Business Card</title>
<link rel="stylesheet" href="https://fonts.googleapis.com/css2?family=Noto+Sans:wght@400;600;700&display=swap">
<style>
  :root {
    --navy: #23255e;
    --blue: #4a86c8;
    --rule-blue: #3f7cc0;
    --ink: #1a1a1a;
    --band: #0d1328;
    --faint: #e2e2e8;
    --faint-edge: #d3d3dc;
    --paper: #ffffff;
  }
  html, body {
    margin: 0;
    padding: 0;
    width: 1200px;
    height: 702px;
    overflow: hidden;
    background: var(--paper);
  }
  .card {
    position: relative;
    width: 1200px;
    height: 702px;
    overflow: hidden;
    background: var(--paper);
    font-family: "Noto Sans", sans-serif;
  }
  .backdrop-mark {
    position: absolute;
    left: 0;
    top: 0;
  }
  .brand-mark {
    position: absolute;
    left: 58px;
    top: 58px;
  }
  .brand-name {
    position: absolute;
    left: 285px;
    top: 112px;
    margin: 0;
    font-size: 64px;
    font-weight: 700;
    line-height: 1;
    color: var(--navy);
    letter-spacing: 0.5px;
  }
  .brand-web {
    position: absolute;
    left: 287px;
    top: 186px;
    margin: 0;
    font-size: 30px;
    font-weight: 400;
    line-height: 1;
    color: var(--blue);
  }
  .person-name {
    position: absolute;
    left: 58px;
    top: 366px;
    margin: 0;
    font-size: 37px;
    font-weight: 700;
    line-height: 1.1;
    color: var(--blue);
    text-transform: uppercase;
  }
  .person-role {
    position: absolute;
    left: 59px;
    top: 412px;
    margin: 0;
    font-size: 24px;
    font-weight: 400;
    color: var(--ink);
  }
  .contact-list {
    position: absolute;
    left: 58px;
    top: 476px;
    margin: 0;
    padding: 0;
    list-style: none;
  }
  .contact-item {
    display: flex;
    align-items: center;
    height: 39.5px;
    font-size: 27px;
    font-weight: 600;
    color: var(--ink);
  }
  .contact-icon {
    width: 30px;
    height: 30px;
    margin-right: 17px;
    flex: none;
  }
  .contact-item.is-phone .contact-text,
  .contact-item.is-fax .contact-text { margin-left: 6px; }
  .footer-rule {
    position: absolute;
    left: 0;
    top: 639px;
    width: 1200px;
    height: 7px;
    background: var(--rule-blue);
  }
  .footer-band {
    position: absolute;
    left: 0;
    top: 646px;
    width: 1200px;
    height: 56px;
    background: var(--band);
  }
</style>
</head>
<body>
  <div class="card">
    <svg class="backdrop-mark" width="1200" height="702" viewBox="0 0 1200 702" role="img" aria-label="Faint large circular emblem decoration">
      <circle cx="1106" cy="487" r="243" fill="var(--faint)" opacity="0.45"/>
      <circle cx="1106" cy="487" r="243" fill="none" stroke="var(--faint-edge)" stroke-width="10"/>
    </svg>

    <svg class="brand-mark" width="218" height="218" viewBox="0 0 218 218" aria-hidden="true">
      <circle cx="109" cy="109" r="104" fill="none" stroke="var(--navy)" stroke-width="9"/>
    </svg>
    <h1 class="brand-name">Pellworth Legal</h1>
    <p class="brand-web">www.pellworthlegal.com.au</p>

    <h2 class="person-name">Declan Pellworth</h2>
    <p class="person-role">Principal</p>

    <ul class="contact-list">
      <li class="contact-item is-phone">
        <svg class="contact-icon" viewBox="0 0 24 24" aria-hidden="true">
          <path fill="var(--rule-blue)" d="M6.6 10.8c1.4 2.8 3.8 5.1 6.6 6.6l2.2-2.2c.3-.3.7-.4 1-.2 1.1.4 2.3.6 3.6.6.6 0 1 .4 1 1V20c0 .6-.4 1-1 1C10.6 21 3 13.4 3 4c0-.6.4-1 1-1h3.5c.6 0 1 .4 1 1 0 1.3.2 2.5.6 3.6.1.3 0 .7-.2 1L6.6 10.8z"/>
        </svg>
        <span class="contact-text">+61 400 555 218</span>
      </li>
      <li class="contact-item is-fax">
        <svg class="contact-icon" viewBox="0 0 24 24" aria-hidden="true">
          <rect x="6" y="2" width="12" height="6" fill="var(--rule-blue)"/>
          <rect x="2" y="8" width="20" height="10" rx="2" fill="var(--rule-blue)"/>
          <rect x="6" y="13" width="12" height="9" fill="#fff" stroke="var(--rule-blue)" stroke-width="1.6"/>
          <line x1="8.5" y1="16.5" x2="15.5" y2="16.5" stroke="var(--rule-blue)" stroke-width="1.4"/>
          <line x1="8.5" y1="19.3" x2="13.5" y2="19.3" stroke="var(--rule-blue)" stroke-width="1.4"/>
        </svg>
        <span class="contact-text">+61 7 3900 5512</span>
      </li>
      <li class="contact-item is-email">
        <svg class="contact-icon" viewBox="0 0 24 24" aria-hidden="true">
          <rect x="2" y="5" width="20" height="14" rx="1.5" fill="var(--rule-blue)"/>
          <path d="M3 6.5l9 6.5 9-6.5" fill="none" stroke="#fff" stroke-width="1.6"/>
        </svg>
        <span class="contact-text">info@pellworthlegal.com.au</span>
      </li>
      <li class="contact-item is-address">
        <svg class="contact-icon" viewBox="0 0 24 24" aria-hidden="true">
          <path fill="var(--rule-blue)" d="M12 3l10 9h-3v9h-5v-6h-4v6H5v-9H2z"/>
        </svg>
        <span class="contact-text">14 Harbourview Rd Wynnum Queensland Australia.</span>
      </li>
    </ul>

    <div class="footer-rule"></div>
    <div class="footer-band" role="img" aria-label="Dark navy footer band with fine dot texture"></div>
  </div>
</body>
</html>
```